Home & Landing Page REDESIGN needed for Psychology Group

We need a redesign for the template home and landing pages for our psychology group.

Ideally we want a similar layout in the core features, but we want a newer, fresher and more professional design overall.

Our developer will implement the changes from the winning design.

Logo to stay the same.

Please ensure you stay within the same color scheme as the LOGOs 3 main colors.

We want to convey professional, modern, friendly and caring.

Here is the main page template:

http://www.quillmindcare.com.au/psychologist-melbourne/

and

http://www.quillmindcare.com.au

*note: we are creating an intro video, please ensure it is included in your brief, near the top of the site* - it is not included on the current site yet but we need it included in all designs.

Target Market(s)

people suffering anxiety, depression or stress that need a psychologist

Industry/Entity Type

Psychology

Number of Pages Required

2 page

Font styles to use
Sans Serif

Colors
86cfc6
85cae6
b7a5cd

Requirements
Must have
• search bar functionality in the top fold of the page, strong focus that we are experienced in anxiety, depression and stress counselling.
• Lots of images and pictures.
• **MUST HAVE: the search square area as it is, unfortunately this cannot be a bar due to development issues with the theme. Please make sure all designs have the search function like it is showing (in a square/rectangle)**
• Must also keep:
• - content area for both home page and city landing pages
• - banner area with search bar same style
• - an area for faqs and blog
• - locations across Australia
• We want most of the same areas, just a refresh so they look better and more polished and professional.
• We are also having an intro video designed, so please include that in your design. (its not in our current web design, but needs to be in the new design)
Should not have
• No orange type colors

```html
<!DOCTYPE html>
<html lang="en">
<head>
<meta charset="utf-8">
<title>Quill Mind Care – Anxiety, Depression &amp; Stress Psychologists</title>
<link href="https://fonts.googleapis.com/css2?family=Lato:wght@300;400;700&family=Open+Sans:wght@400;600&display=swap" rel="stylesheet">
<style>
:root{
  --teal:#86cfc6;
  --teal-deep:#3fa99c;
  --sky:#85cae6;
  --lilac:#b7a5cd;
  --lilac-deep:#8f7fbf;
  --violet-text:#6b62a8;
  --navy:#1d3450;
  --ink:#2b2b2b;
  --muted:#7a7a7a;
  --band:#eef5fc;
  --white:#ffffff;
  --line:#e3e3e3;
}
*{box-sizing:border-box;margin:0;padding:0}
html,body{width:1200px;height:2691px;overflow:hidden;background:var(--white)}
body{position:relative;font-family:"Open Sans",Arial,sans-serif;color:var(--ink)}
.abs{position:absolute}
a{color:inherit;text-decoration:none}

/* header */
.brand{left:133px;top:46px;display:flex;align-items:center;gap:14px}
.brand-dot{width:64px;height:64px;border-radius:50%;background:var(--teal)}
.brand-text{font-family:"Lato",sans-serif;font-weight:700;font-size:30px;color:var(--navy);line-height:1}
.top-links{right:133px;top:30px;font-size:12px;color:#444;display:flex;gap:10px}
.top-links span.sep{color:#999}
.btn-appointment{left:867px;top:79px;width:200px;height:39px;background:var(--navy);color:var(--white);font-size:12px;font-weight:600;display:flex;align-items:center;justify-content:center;gap:10px;letter-spacing:.3px}

/* nav */
.main-nav{left:0;top:151px;width:1200px;height:41px;background:var(--lilac)}
.main-nav ul{list-style:none;position:absolute;left:133px;top:0;height:41px;display:flex}
.main-nav li{height:41px;display:flex;align-items:center;padding:0 27px;color:var(--white);font-family:"Lato",sans-serif;font-size:12.5px;letter-spacing:.5px}
.main-nav li.active{background:var(--lilac-deep)}

/* hero */
.hero{left:0;top:192px;width:1200px;height:422px;background:linear-gradient(90deg,#e8eef3 0%,#bfe3ef 30%,#7fcbe0 55%,#a8dbe6 75%,#d6ecf1 100%)}
.hero-figure{left:170px;top:192px;width:280px;height:422px;background:linear-gradient(90deg,rgba(244,243,240,0) 0%,#f4f3f0 30%,#ece8e2 70%,rgba(230,226,220,0) 100%)}
.hero-play{left:579px;top:382px}
.hero-caption{left:420px;top:440px;width:352px;text-align:center;font-family:"Lato",sans-serif;font-size:20px;line-height:27px;color:#2f3b48}
.hero-arrow{top:392px}
.search-box{left:786px;top:235px;width:281px;height:335px;background:var(--teal);padding:16px 20px}
.search-title{font-family:"Lato",sans-serif;font-weight:700;font-size:22px;color:var(--white);letter-spacing:.5px}
.search-field{position:absolute;left:20px;width:241px;height:39px;background:var(--white);font-size:11px;color:#555;display:flex;align-items:center;justify-content:space-between;padding:0 12px}
.search-range{position:absolute;left:20px;top:218px;font-size:10px;color:var(--white)}
.search-btn{position:absolute;left:20px;top:274px;width:89px;height:38px;background:var(--lilac-deep);color:var(--white);font-family:"Lato",sans-serif;font-weight:700;font-size:13px;display:flex;align-items:center;justify-content:center;letter-spacing:.5px}

/* intro */
.intro-title{left:123px;top:668px;width:954px;text-align:center;font-family:"Lato",sans-serif;font-size:21.5px;line-height:30px;color:var(--teal-deep);font-weight:400}
.intro-sub{left:133px;top:748px;width:934px;text-align:center;font-family:"Lato",sans-serif;font-size:16px;color:var(--muted)}

/* services */
.service{top:811px;width:298px}
.service-photo{width:298px;height:181px}
.service-title{margin-top:16px;text-align:center;font-family:"Lato",sans-serif;font-size:16px;color:var(--teal-deep);letter-spacing:.5px;font-weight:400}
.service-text{margin-top:6px;text-align:center;font-size:10.5px;line-height:16px;color:#555}
.outline-btn{position:absolute;border:1px solid var(--violet-text);color:var(--violet-text);font-family:"Lato",sans-serif;font-size:13px;display:flex;align-items:center;justify-content:center}

/* understanding band */
.band{left:0;width:1200px;background:var(--band)}
.band-title{left:133px;top:1358px;width:934px;text-align:center;font-family:"Lato",sans-serif;font-size:21px;color:var(--violet-text);font-weight:400}
.band-text{left:133px;top:1398px;width:934px;text-align:center;font-size:9.5px;line-height:16px;color:#555}
.grey-btn{position:absolute;border:1px solid #9a9a9a;color:#666;font-family:"Lato",sans-serif;font-size:15px;display:flex;align-items:center;justify-content:center;background:transparent}

/* guarantee / faq */
.col-title{font-family:"Lato",sans-serif;font-size:20px;color:var(--teal-deep);letter-spacing:.5px;font-weight:400}
.col-lead{font-size:12.5px;font-weight:600;color:#222}
.col-text{font-size:10px;line-height:18px;color:#666}
.round-arrow{width:20px;height:20px;border-radius:50%;background:#cfcfcf;display:flex;align-items:center;justify-content:center}

/* blog */
.blog-title{left:133px;top:1952px;font-family:"Lato",sans-serif;font-size:20px;color:var(--teal-deep);font-weight:400}
.post{top:2000px;width:298px}
.post-photo{position:relative;width:298px;height:174px}
.post-date{position:absolute;left:0;bottom:0;width:54px;height:56px;background:var(--sky);color:var(--white);text-align:center;font-family:"Lato",sans-serif;padding-top:8px}
.post-date b{display:block;font-size:19px;font-weight:400;line-height:22px}
.post-date small{font-size:8px;letter-spacing:1px}
.post-heading{margin-top:22px;font-family:"Lato",sans-serif;font-size:15.5px;line-height:22px;color:#222;font-weight:400}
.post-more{margin-top:10px;font-size:9.5px;color:var(--lilac-deep);letter-spacing:.5px}

/* cta */
.cta-title{left:133px;top:2400px;width:934px;text-align:center;font-family:"Lato",sans-serif;font-size:20px;color:var(--violet-text);font-weight:400}
.cta-text{left:133px;top:2437px;width:934px;text-align:center;font-size:10px;color:#555}

/* footer */
.footer-links{left:133px;top:2612px;font-size:10.5px;color:#444;display:flex;gap:8px}
.footer-copy{left:133px;top:2638px;font-size:10.5px;color:#444}
.social{top:2622px;width:26px;height:26px;border-radius:50%}
</style>
</head>
<body>

<!-- header -->
<div class="abs brand"><span class="brand-dot"></span><span class="brand-text">Quill Mind Care</span></div>
<nav class="abs top-links"><a>About Us</a><span class="sep">|</span><a>Therapies We Use</a><span class="sep">|</span><a>Join Our Associate Program</a><span class="sep">|</span><a>Blog</a></nav>
<a class="abs btn-appointment">
  <svg width="14" height="14" viewBox="0 0 14 14" aria-hidden="true"><rect x="1" y="2.5" width="12" height="10.5" fill="none" stroke="#fff" stroke-width="1.4"/><line x1="1" y1="6" x2="13" y2="6" stroke="#fff" stroke-width="1.4"/><line x1="4" y1="0.5" x2="4" y2="4" stroke="#fff" stroke-width="1.4"/><line x1="10" y1="0.5" x2="10" y2="4" stroke="#fff" stroke-width="1.4"/></svg>
  MAKE AN APPOINTMENT
</a>

<nav class="abs main-nav">
  <ul>
    <li class="active">HOME</li>
    <li>COUNSELLING TYPES</li>
    <li>PSYCHOLOGIST LOCATIONS</li>
    <li>FAQS</li>
    <li>FEES &amp; REBATES</li>
    <li>QUIZZES</li>
    <li>CONTACT</li>
  </ul>
</nav>

<!-- hero -->
<section class="abs hero" role="img" aria-label="Intro video still: woman in a white dress and sun hat on a bright beach"></section>
<div class="abs hero-figure" role="img" aria-label="Woman in white dress holding a flowing scarf"></div>
<svg class="abs hero-play" width="40" height="40" viewBox="0 0 40 40" aria-label="Play intro video"><circle cx="20" cy="20" r="20" fill="#6b5aa6"/><polygon points="15,11 30,20 15,29" fill="#fff"/></svg>
<div class="abs hero-caption">Experienced and Caring Anxiety &amp;<br>Depression Psychologists</div>
<svg class="abs hero-arrow" style="left:22px" width="14" height="24" viewBox="0 0 14 24" aria-hidden="true"><polyline points="12,2 2,12 12,22" fill="none" stroke="#fff" stroke-width="2"/></svg>
<svg class="abs hero-arrow" style="left:1162px" width="14" height="24" viewBox="0 0 14 24" aria-hidden="true"><polyline points="2,2 12,12 2,22" fill="none" stroke="#555" stroke-width="2"/></svg>

<form class="abs search-box">
  <div class="search-title">SEARCH FOR</div>
  <div class="search-field" style="top:52px">Type of Counselling<svg width="9" height="6" viewBox="0 0 9 6"><polyline points="1,1 4.5,5 8,1" fill="none" stroke="#555" stroke-width="1.3"/></svg></div>
  <div class="search-field" style="top:108px">Location<svg width="9" height="6" viewBox="0 0 9 6"><polyline points="1,1 4.5,5 8,1" fill="none" stroke="#555" stroke-width="1.3"/></svg></div>
  <div class="search-field" style="top:164px">Enter your suburb<svg width="9" height="6" viewBox="0 0 9 6"><polyline points="1,1 4.5,5 8,1" fill="none" stroke="#555" stroke-width="1.3"/></svg></div>
  <div class="search-range">Search in radius 50 kilometers</div>
  <svg style="position:absolute;left:20px;top:234px" width="241" height="14" viewBox="0 0 241 14" aria-hidden="true"><line x1="0" y1="7" x2="241" y2="7" stroke="#fff" stroke-width="3"/><line x1="0" y1="7" x2="88" y2="7" stroke="#6b5aa6" stroke-width="3"/><circle cx="90" cy="7" r="6" fill="#fff" stroke="#6b5aa6" stroke-width="2"/></svg>
  <div class="search-btn">SEARCH</div>
</form>

<!-- intro -->
<h1 class="abs intro-title">We are psychologists passionate about helping you overcome your depression, anxiety and stress and<br>create a life you love.</h1>
<p class="abs intro-sub">Our experienced psychologists can help you with...</p>

<article class="abs service" style="left:133px">
  <div class="service-photo" role="img" aria-label="Woman sitting on a bed with her head lowered" style="background:linear-gradient(135deg,#a8734e,#e4d6c8)"></div>
  <h2 class="service-title">DEPRESSION COUNSELLING</h2>
  <p class="service-text">Are you feeling empty, hopeless and despairing? Do you have huge ups and downs? Or do you have Male depression (discontented with yourself, antagonistic, exaggerated behaviour &amp; avoidance) or post baby blues?</p>
</article>
<article class="abs service" style="left:451px">
  <div class="service-photo" role="img" aria-label="Worried woman resting her face against her hand" style="background:linear-gradient(135deg,#2f5a3c,#a9b98a)"></div>
  <h2 class="service-title">ANXIETY COUNSELLING</h2>
  <p class="service-text">Do you feel tense, edgy and wound up? Do you worry a lot, or think in obsessive ways? Do you avoid situations that make you anxious? Do you sometimes have panic attacks? Are you still affected by a past trauma? We can help</p>
</article>
<article class="abs service" style="left:769px">
  <div class="service-photo" role="img" aria-label="Stressed man at a desk with a laptop" style="background:linear-gradient(135deg,#c8b7a4,#4a5a6e)"></div>
  <h2 class="service-title">STRESS COUNSELLING</h2>
  <p class="service-text">Do you feel tired but also still wired up? Do you struggle with too many expectations? Are you exhausted and close to burnout? Do you have trouble sleeping and/or relaxing? Is there no fun in your life? We can help you.</p>
</article>

<a class="outline-btn" style="left:133px;top:1119px;width:298px;height:44px">Take our Depression Quiz now</a>
<a class="outline-btn" style="left:451px;top:1119px;width:298px;height:44px">Take our Anxiety Quiz now</a>
<a class="outline-btn" style="left:769px;top:1119px;width:298px;height:44px">Take our Stress Quiz now</a>
<a class="outline-btn" style="left:133px;top:1175px;width:298px;height:44px">Take our MALE Depression Quiz now</a>

<!-- understanding -->
<section class="abs band" style="top:1308px;height:264px"></section>
<h2 class="abs band-title">Understanding Psychologists Experienced in Depression and Anxiety Counselling</h2>
<p class="abs band-text">We at Quill Mind Care are a team of Australian Psychologists specialising in helping you with Anxiety, Depression and Stress, and all forms and combinations of these.<br>It is our vision to be the go-to place for any Australians suffering from Anxiety and Depression to gain the most helpful counselling available today in overcoming these very common problems.<br>Almost a quarter of all Australians suffer from Anxiety or depression at some time in their life.</p>
<a class="grey-btn" style="left:499px;top:1471px;width:201px;height:45px">We are here to help</a>

<!-- guarantee -->
<section class="abs" style="left:133px;top:1652px;width:430px">
  <h2 class="col-title">GREAT MATCH GUARANTEE</h2>
  <p class="col-lead" style="margin-top:16px">We know how important it is to find the right psychologist to help.</p>
  <p class="col-text" style="margin-top:14px">Call our Client Care Consultants to be personally matched with one of our psychologists.</p>
  <p class="col-text" style="margin-top:16px">After your first session, if you don't feel the psychologist is the right fit, we will re-match you and provide a complimentary next session.</p>
</section>
<a class="outline-btn" style="left:133px;top:1830px;width:172px;height:45px">Find Your Match Now</a>

<!-- faq -->
<section class="abs" style="left:633px;top:1652px;width:434px">
  <h2 class="col-title">FAQ's</h2>
  <p class="col-lead" style="margin-top:16px">Exciting news in Treating Anxiety and Depression</p>
  <p class="col-text" style="margin-top:14px">In recent years there has been a huge amount of research in neuroscience with exciting new discoveries into what is happening in the brain when you are experiencing depression and anxiety and why you are suffering in these ways. This enables us to create wonderful new methodologies for helping you overcome these problems. The newer methodologies of Mindfulness and Compassionate Therapy are showing extremely positive results. So you do not have to continue to suffer. We now have very powerful and proven methods for helping you overcome anxiety, stress and depression that don't have you relying solely on medication.</p>
</section>
<div class="abs round-arrow" style="left:1043px;top:1657px"><svg width="8" height="10" viewBox="0 0 8 10"><polyline points="2,1 6,5 2,9" fill="none" stroke="#fff" stroke-width="1.6"/></svg></div>

<!-- blog -->
<h2 class="abs blog-title">Blog</h2>
<div class="abs round-arrow" style="left:1019px;top:1956px;background:#e2e2e2"><svg width="8" height="10" viewBox="0 0 8 10"><polyline points="6,1 2,5 6,9" fill="none" stroke="#fff" stroke-width="1.6"/></svg></div>
<div class="abs round-arrow" style="left:1043px;top:1956px;background:#9a9a9a"><svg width="8" height="10" viewBox="0 0 8 10"><polyline points="2,1 6,5 2,9" fill="none" stroke="#fff" stroke-width="1.6"/></svg></div>

<article class="abs post" style="left:133px">
  <div class="post-photo" role="img" aria-label="Woman holding her head with a headache" style="background:linear-gradient(135deg,#d9d6cf,#b8a893)"><div class="post-date"><b>30</b><small>NOV</small></div></div>
  <h3 class="post-heading">Pellentesque ac orci ut nulla maximus eleifend sed et ligula</h3>
  <p class="post-more">READ MORE</p>
</article>
<article class="abs post" style="left:451px">
  <div class="post-photo" role="img" aria-label="Man shouting through a megaphone at a woman covering her ears" style="background:linear-gradient(135deg,#9a9a9a,#cfcfcf)"><div class="post-date"><b>30</b><small>NOV</small></div></div>
  <h3 class="post-heading">Pellentesque ac orci ut nulla maximus eleifend sed et ligula</h3>
  <p class="post-more">READ MORE</p>
</article>
<article class="abs post" style="left:769px">
  <div class="post-photo" role="img" aria-label="Tired woman resting her head on a table" style="background:linear-gradient(135deg,#e2c8a8,#8a6a4e)"><div class="post-date"><b>30</b><small>NOV</small></div></div>
  <h3 class="post-heading">Pellentesque ac orci ut nulla maximus eleifend sed et ligula</h3>
  <p class="post-more">READ MORE</p>
</article>

<!-- call to action -->
<section class="abs band" style="top:2339px;height:241px"></section>
<h2 class="abs cta-title">Ready to get started?</h2>
<p class="abs cta-text">Every day across Australia, millions of people struggle with depression, anxiety and stress. We're passionate about changing that.</p>
<a class="grey-btn" style="left:483px;top:2469px;width:235px;height:44px">Request an Appointment</a>

<!-- footer -->
<nav class="abs footer-links"><a>Home</a><span>|</span><a>Counselling Types</a><span>|</span><a>Pshychologist Locations</a><span>|</span><a>FAQs</a><span>|</span><a>Fees &amp; Rebates</a><span>|</span><a>Quizzes</a><span>|</span><a>Contact</a></nav>
<p class="abs footer-copy">Copyright © 2016 Company name. All rights reserved.</p>
<span class="abs social" style="left:1010px;background:#3b5c9a" aria-label="Social link"></span>
<span class="abs social" style="left:1040px;background:#2f9fe0" aria-label="Social link"></span>

</body>
</html>
```